Event Newsletter for Financial Advisors

Create a newsletter that only goes out to our field financial advisors.

Creating awareness around upcoming events, highlighting past events with pictures/video, and linking registrations to the newsletter.

```html
<!DOCTYPE html>
<html lang="en">
<head>
<meta charset="utf-8">
<title>Ledgerline – Advisor Events Newsletter</title>
<link href="https://fonts.googleapis.com/css2?family=Lato:wght@400;700&family=Rubik:wght@500;600;700&display=swap" rel="stylesheet">
<style>
:root{
  --navy:#1f2a4d;
  --navy-light:#2a365c;
  --gold:#e9c53a;
  --white:#ffffff;
  --ink:#2b2b2b;
  --muted:#7a7a7a;
  --rule:#c9a92c;
}
*{box-sizing:border-box;margin:0;padding:0}
html,body{width:1200px;height:4628px;overflow:hidden}
body{position:relative;background:var(--white);font-family:'Lato',sans-serif;color:var(--ink)}
.abs{position:absolute}
.top-rule{left:0;top:0;width:1200px;height:14px;background:var(--gold)}
.masthead{left:0;top:14px;width:1200px;height:176px;background:var(--navy);display:flex;align-items:center;justify-content:center;gap:22px}
.brand-mark{width:34px;height:34px;background:var(--gold)}
.brand-name{font-family:'Rubik',sans-serif;font-weight:600;font-size:52px;color:var(--white);letter-spacing:1px}
.photo{background:linear-gradient(135deg,#5a5a5a,#9c9c9c 45%,#3e3e3e)}
.hero{left:0;top:190px;width:1200px;height:884px}
.upcoming{left:666px;top:860px;width:473px;height:826px;background:var(--gold);padding:15px 13px 0}
.upcoming-title{background:var(--navy);height:75px;display:flex;align-items:center;justify-content:center;font-family:'Rubik',sans-serif;font-weight:600;font-size:36px;color:var(--gold)}
.event-list{list-style:none;padding:0 12px}
.event{padding:30px 12px 32px;border-bottom:2px solid var(--rule)}
.event:last-child{border-bottom:none}
.event p{font-size:25px;line-height:42px;color:var(--navy);font-weight:500}
.event .date{display:inline-block;margin-top:10px;background:var(--navy);color:var(--gold);font-size:16px;font-weight:700;padding:5px 6px}
.side-photo{left:666px;top:1738px;width:473px;height:408px}
.about{left:58px;top:1146px;width:527px}
.about .kicker{font-family:'Rubik',sans-serif;font-weight:600;font-size:48px;color:var(--gold);line-height:60px}
.about h1{font-family:'Rubik',sans-serif;font-weight:600;font-size:50px;color:var(--navy);line-height:70px;white-space:nowrap;letter-spacing:.5px}
.about p{margin-top:16px;font-size:27px;line-height:54px;text-align:justify;color:#3a3a3a}
.about p+p{margin-top:54px}
.past-band{left:0;top:2247px;width:1200px;height:411px;background:linear-gradient(120deg,var(--navy) 0%,var(--navy) 55%,var(--navy-light) 62%,var(--navy) 70%,var(--navy-light) 85%,var(--navy) 100%)}
.past-title{left:0;top:2318px;width:1200px;text-align:center;font-family:'Rubik',sans-serif;font-weight:600;font-size:51px;color:var(--white);letter-spacing:1px}
.past-title span{color:var(--gold)}
.past-card{width:510px;height:573px}
.past-card .card-photo{position:absolute;left:0;top:0;width:510px;height:300px}
.past-card .card-body{position:absolute;left:33px;top:213px;width:445px;height:272px;background:var(--white);border-bottom:6px solid var(--gold);text-align:center;padding-top:28px;box-shadow:0 4px 14px rgba(0,0,0,.08)}
.card-body .date{font-size:22px;color:var(--ink)}
.card-body h3{margin-top:14px;font-weight:500;font-size:27px;line-height:42px;color:#1b1b1b}
.card-body p{margin-top:14px;font-size:18px;line-height:35px;color:var(--muted)}
.newsletter{left:59px;top:4090px;width:1080px;height:413px;background:linear-gradient(120deg,var(--navy) 0%,var(--navy) 50%,var(--navy-light) 60%,var(--navy) 72%,var(--navy-light) 88%,var(--navy) 100%)}
.newsletter h2{position:absolute;left:0;top:60px;width:100%;text-align:center;font-family:'Rubik',sans-serif;font-weight:600;font-size:51px;color:var(--white);letter-spacing:1px}
.email-field{position:absolute;left:43px;top:159px;width:995px;height:74px;background:var(--white);font-size:22px;color:#333;display:flex;align-items:center;padding-left:20px}
.subscribe{position:absolute;left:417px;top:287px;width:246px;height:72px;background:var(--gold);border:3px solid var(--white);display:flex;align-items:center;justify-content:center;font-family:'Rubik',sans-serif;font-weight:600;font-size:21px;color:var(--navy)}
.footer{left:0;top:4503px;width:1200px;height:125px;background:var(--gold);display:flex;align-items:center;justify-content:center;font-family:'Rubik',sans-serif;font-weight:600;font-size:21px;color:var(--navy);padding-bottom:12px}
</style>
</head>
<body>
<div class="abs top-rule"></div>
<header class="abs masthead">
  <span class="brand-mark"></span>
  <span class="brand-name">LEDGERLINE</span>
</header>

<div class="abs hero photo" role="img" aria-label="Black and white photo of two advisors reviewing a document at a desk"></div>

<section class="abs upcoming">
  <div class="upcoming-title">UPCOMING EVENTS</div>
  <ul class="event-list">
    <li class="event"><p>Temporibus autem quibusdam et fiis debitis aut rerum itatbus saepe eveniet</p><span class="date">02 JUNE 2024</span></li>
    <li class="event"><p>Emporibus autem quibusdam et fiis debitis aut rerum itatbus saepe eveniet</p><span class="date">04 JUNE 2024</span></li>
    <li class="event"><p>Mporibus autem quibusdam et fiis debitis aut rerum itatbus saepe eveniet</p><span class="date">07 JUNE 2024</span></li>
  </ul>
</section>

<div class="abs side-photo photo" role="img" aria-label="Black and white photo of smiling colleagues in a meeting"></div>

<section class="abs about">
  <div class="kicker">ABOUT</div>
  <h1>FINANCIAL ADVISORS</h1>
  <p>Nam libero tempore, cum soluta nobis est eligendi optio cumque nihil impedit quo minus id quod maxime placeat facere possimus, omnis voluptas assumenda est, omnis dolor repellendus. Temporibus autem quibusdam et aut officiis debitis aut rerum necessitatibus saepe eveniet ut et voluptates repudiandae sint et molestiae non recusandae.</p>
  <p>Itaque earum rerum hic tenetur a sapiente delectus, ut aut reiciendis dignissimos ducimus qui blanditiis praesentium voluptatum deleniti atque corrupti voluptatibus maiores alias consequatur aut perferendis doloribus asperiores repellat.</p>
</section>

<div class="abs past-band"></div>
<h2 class="abs past-title"><span>OUR</span> PAST EVENTS</h2>

<article class="abs past-card" style="left:59px;top:2425px">
  <div class="card-photo photo" role="img" aria-label="Photo of advisors in a seated discussion"></div>
  <div class="card-body"><div class="date">25 May 2024</div><h3>Itaque earum rerum hic tenetur<br>a sapiente delectus</h3><p>Reiciendis voluptatibus maiores alias conseq<br>uatur aut perferendis dres repellat.</p></div>
</article>
<article class="abs past-card" style="left:630px;top:2425px">
  <div class="card-photo photo" role="img" aria-label="Photo of a team laughing together"></div>
  <div class="card-body"><div class="date">21 May 2024</div><h3>Taque earum rerum hic tenetur<br>a sapiente delectus</h3><p>Reiciendis voluptatibus maiores alias conseq<br>uatur aut perferendis dres repellat.</p></div>
</article>
<article class="abs past-card" style="left:59px;top:2967px">
  <div class="card-photo photo" role="img" aria-label="Photo of an advisor smiling in a client meeting"></div>
  <div class="card-body"><div class="date">18 May 2024</div><h3>Aque earum rerum hic tenetur<br>a sapiente delectus</h3><p>Reiciendis voluptatibus maiores alias conseq<br>uatur aut perferendis dres repellat.</p></div>
</article>
<article class="abs past-card" style="left:630px;top:2967px">
  <div class="card-photo photo" role="img" aria-label="Photo of an advisor presenting at a table"></div>
  <div class="card-body"><div class="date">08 April 2024</div><h3>Que earum rerum hic tenetur<br>a sapiente delectus</h3><p>Reiciendis voluptatibus maiores alias conseq<br>uatur aut perferendis dres repellat.</p></div>
</article>
<article class="abs past-card" style="left:59px;top:3513px">
  <div class="card-photo photo" role="img" aria-label="Photo of clients reviewing papers with an advisor"></div>
  <div class="card-body"><div class="date">04 April 2024</div><h3>Earum rerum hic tenetur<br>a sapiente delectus</h3><p>Reiciendis voluptatibus maiores alias conseq<br>uatur aut perferendis dres repellat.</p></div>
</article>
<article class="abs past-card" style="left:630px;top:3513px">
  <div class="card-photo photo" role="img" aria-label="Photo of an advisor at an office meeting"></div>
  <div class="card-body"><div class="date">03 March 2024</div><h3>Arum rerum hic tenetur<br>a sapiente delectus</h3><p>Reiciendis voluptatibus maiores alias conseq<br>uatur aut perferendis dres repellat.</p></div>
</article>

<section class="abs newsletter">
  <h2>OUR NEWSLETTER</h2>
  <div class="email-field">Enter The Email</div>
  <div class="subscribe">SUBSCRIBE US</div>
</section>

<footer class="abs footer">COPYRIGHTS@2024.LEDGERLINE.ALL RIGHTS RESERVED</footer>
</body>
</html>
```